Hello my name is Colin, I am Starting a business called Harbor Health and fitness and am in need of a memorable business card.
It is a personal training studio. I have added the logo that i would like to be on the left center om my business card. i would like room left up the top for a heading sentence such as. "Is your body shocking for all the wrong reasons". there must be room left on the right of the logo below the main heading for 3 sub headings.
then under those 3 headings and logo room for another larger heading eg. "give me a call and learn how to eat chocolate, drink bear and have great sex". in what room is left i would like to be used for my contact details, use I'm Colin Fairweather your fitness expert on the left then on the right Phone, Email and website space in at least 12 Point. Very specific i know :) now onto the back, for the back i would like an eye catching graphic and room for one main headline and 3 bullet points centered just write anything i will choose what to put in them when i pick a winner. Thank you very much for sticking through all of that :) i appreciate you taking the time to read it and hopefully undergo designing me a business card.
I can't wait to see the designs!

Target Market(s)

slightly more towards females although it would probably be best if it was targeted towards both sexes

Industry/Entity Type

Training

Requirements
Nice to have
• I would love to see if anyone could come up with a design that would really make my card stand out and be memorable.
Should not have
• tacky fitness photos of abs and muscles etc.

```html
<!DOCTYPE html>
<html lang="en">
<head>
<meta charset="utf-8">
<title>Harbor Health and Fitness – Business Card</title>
<link rel="stylesheet" href="https://fonts.googleapis.com/css2?family=Didact+Gothic&family=Encode+Sans+Condensed:wght@300;400&display=swap">
<style>
  :root {
    --page: #ffffff;
    --card: #ffffff;
    --card-edge: #9a9a9a;
    --card-shadow: #b9b9b9;
    --ink: #111111;
    --ink-soft: #333333;
    --placeholder: #2a2a2a;
  }
  * { margin: 0; padding: 0; box-sizing: border-box; }
  html, body {
    width: 1200px; height: 750px; overflow: hidden;
    background: var(--page);
    font-family: "Didact Gothic", "Century Gothic", sans-serif;
    color: var(--ink);
  }
  .canvas { position: relative; width: 1200px; height: 750px; }
  .card {
    position: absolute; left: 82px; top: 88px; width: 1034px; height: 590px;
    background: var(--card);
    border: 1px solid var(--card-edge);
    box-shadow: 6px 6px 0 var(--card-shadow);
  }
  .abs { position: absolute; white-space: nowrap; }

  .front-heading {
    left: 15px; top: 8px;
    font-family: "Encode Sans Condensed", "Arial Narrow", sans-serif;
    font-weight: 300; font-size: 31px; letter-spacing: -0.2px;
  }
  .brand { text-align: center; line-height: 1; font-weight: 400; color: var(--ink); }
  .brand-main { left: 58px; top: 58px; width: 240px; }
  .brand-main .brand-name { font-size: 64px; letter-spacing: -1px; }
  .brand-main .brand-tag { font-size: 17px; margin-top: 6px; }
  .brand-small { left: 650px; top: 360px; width: 80px; }
  .brand-small .brand-name { font-size: 21px; letter-spacing: -0.5px; }
  .brand-small .brand-tag { font-size: 6px; margin-top: 2px; }

  .bullet-list { list-style: none; }
  .bullet-list li { position: relative; height: 33px; }
  .bullet-list li::before {
    content: ""; position: absolute; left: 0; top: 0;
    width: 12px; height: 12px; border-radius: 50%; background: var(--ink);
  }
  .bullet-list li::after {
    content: ""; position: absolute; left: 21px; top: 4px;
    height: 4px; background: var(--ink);
  }
  .front-bullets { left: 330px; top: 67px; }
  .front-bullets li::after { width: 136px; }
  .back-bullets { left: 774px; top: 407px; }
  .back-bullets li { height: 32.5px; }
  .back-bullets li::after { width: 131px; }

  .call-to-action {
    left: 0; top: 161px; width: 536px; text-align: center;
    font-size: 21px; line-height: 25px; white-space: normal; letter-spacing: 0.3px;
  }
  .trainer-intro { left: 12px; top: 238px; }
  .trainer-name { font-size: 16px; margin-left: 23px; letter-spacing: 0.3px; }
  .trainer-role { font-size: 26px; line-height: 28px; letter-spacing: 0.3px; }

  .contact { font-size: 15.5px; line-height: 18px; color: var(--ink-soft); }
  .front-contact { left: 316px; top: 244px; }
  .back-contact { left: 679px; top: 523px; }

  .back-headline {
    left: 748px; top: 335px;
    font-size: 29px; letter-spacing: 0.8px; font-weight: 400;
  }
  .headline-rule {
    left: 735px; top: 365px; width: 284px; height: 2px; background: var(--ink);
  }
  .back-graphic {
    left: 654px; top: 426px; width: 108px; height: 67px;
    background: var(--placeholder); border-radius: 6px;
  }
</style>
</head>
<body>
<div class="canvas">
  <section class="card">
    <!-- Front side -->
    <h1 class="abs front-heading">Is your body shocking for all the wrong reasons?</h1>

    <div class="abs brand brand-main">
      <div class="brand-name">Harbor</div>
      <div class="brand-tag">Health and Fitness</div>
    </div>

    <ul class="abs bullet-list front-bullets" aria-label="Sub headings">
      <li></li><li></li><li></li>
    </ul>

    <p class="abs call-to-action">Give me a call and learn how to eat chocolate, drink bear and have great sex</p>

    <div class="abs trainer-intro">
      <div class="trainer-name">I'm Colin Fairweather</div>
      <div class="trainer-role">your fitness expert</div>
    </div>

    <div class="abs contact front-contact">
      <div>Phone:</div>
      <div>Email:</div>
      <div>Website:</div>
    </div>

    <!-- Back side -->
    <h2 class="abs back-headline">MAIN HEADLINE</h2>
    <div class="abs headline-rule"></div>

    <div class="abs brand brand-small">
      <div class="brand-name">Harbor</div>
      <div class="brand-tag">Health and Fitness</div>
    </div>

    <div class="abs back-graphic" role="img" aria-label="Graphic of a figure lifting a barbell with a fork at one end"></div>

    <ul class="abs bullet-list back-bullets" aria-label="Bullet points">
      <li></li><li></li><li></li>
    </ul>

    <div class="abs contact back-contact">
      <div>Phone:</div>
      <div>Email:</div>
      <div>Website:</div>
    </div>
  </section>
</div>
</body>
</html>
```